Business Card Design

We are state certified residental contractors who specialize in insurance claims. We are insurance restoration experts and have a state multi-lines insurance adjusters license #W584130. We produce insurance grade estimates using the most widely used software in the industry. Our goal is to work for our customers! not the insurance company. Our edge is we don't take short cuts to please the adjuster/insurance company to insure future claims from them. We are experts at restoring damaged properties.from wind, water ,fire and smoke. We pride ourselfs on evaluating damages properly and providing extremely detailed estimates for restoration.We are also educated and experienced in identifiying and correcting indoor air quality issues as a result of common perils and defective materials. .We are not a franchise and are family owned and operated. We provide quality work using only the best local tradesman. We ourselfs are local tradesmen and helped build and restore our community over the past 30 years. We know first hand how our homes were built and are aware of many of the common problems that exist and how to address them. We are licensed insured and bonded.
Industry/Entity Type
Business
Contact Information for Business Card
Beacon Harbor LLC
Marcus Pelley
4185 Willowbend Rd unit K
Coral Point FL.32990 Manager/State Certified Residental Contractor license# CRC5871642
321-555-0187 Office
321-555-0162 Fax

```html
<!DOCTYPE html>
<html lang="en">
<head>
<meta charset="utf-8">
<title>Beacon Harbor LLC — Business Card</title>
<link rel="stylesheet" href="https://fonts.googleapis.com/css2?family=Bebas+Neue&family=Exo+2:wght@300&family=Oswald:wght@300;400&display=swap">
<style>
  :root {
    --ink: #1e1e1e;
    --paper: #ffffff;
    --card-dark: #242424;
    --accent: #8cc63f;
    --backdrop: #e6e4e1;
    --band: #2b2b2b;
  }
  * { box-sizing: border-box; margin: 0; padding: 0; }
  html, body {
    width: 1200px; height: 800px; overflow: hidden;
    background: var(--backdrop);
    font-family: "Oswald", "Arial Narrow", sans-serif;
    color: var(--ink);
  }
  .stage {
    width: 1200px; height: 800px;
    display: flex; align-items: center; justify-content: center; gap: 40px;
  }
  .card {
    position: relative;
    width: 525px; height: 300px;
    box-shadow: 0 6px 18px rgba(0,0,0,.18);
    overflow: hidden;
  }

  /* Back side */
  .card--back {
    background: linear-gradient(160deg, #2e2e2e 0%, var(--card-dark) 55%, #1a1a1a 100%);
    display: flex; align-items: center; justify-content: center;
  }
  .brand { display: flex; align-items: flex-start; gap: 10px; }
  .brand__square {
    width: 16px; height: 16px; background: var(--accent); flex: none; margin-top: 4px;
  }
  .brand__name {
    font-family: "Exo 2", "Arial", sans-serif;
    font-weight: 300; line-height: 1.05;
  }
  .card--back .brand__name { color: var(--paper); font-size: 30px; }

  /* Front side */
  .card--front { background: var(--paper); }
  .card--front .brand { position: absolute; left: 40px; top: 70px; }
  .card--front .brand__name { color: var(--ink); font-size: 28px; }

  .divider {
    position: absolute; left: 262px; top: 58px;
    width: 2px; height: 160px; background: var(--ink);
  }
  .contact {
    position: absolute; left: 282px; top: 64px; right: 14px;
    text-transform: uppercase;
  }
  .contact__name {
    font-family: "Bebas Neue", "Oswald", sans-serif;
    font-weight: 400; font-size: 32px; letter-spacing: .5px; line-height: 1;
  }
  .contact__role {
    font-weight: 400; font-size: 10px; letter-spacing: 6px; margin-top: 2px;
  }
  .contact__lines {
    list-style: none; margin-top: 10px;
    font-weight: 300; font-size: 13px; line-height: 1.45; letter-spacing: .3px;
    white-space: nowrap;
  }
  .license {
    position: absolute; left: 262px; right: 0; top: 224px; height: 24px;
    background: var(--band); color: var(--paper);
    display: flex; align-items: center; padding-left: 12px;
    font-weight: 400; font-size: 13px; letter-spacing: 3px; text-transform: uppercase;
  }
</style>
</head>
<body>
<main class="stage">
  <section class="card card--back" aria-label="Card back">
    <div class="brand">
      <span class="brand__square"></span>
      <span class="brand__name">Beacon Harbor LLC</span>
    </div>
  </section>

  <section class="card card--front" aria-label="Card front">
    <div class="brand">
      <span class="brand__square"></span>
      <span class="brand__name">Beacon<br>Harbor<br>LLC</span>
    </div>
    <div class="divider"></div>
    <div class="contact">
      <h1 class="contact__name">Marcus Pelley</h1>
      <p class="contact__role">Manager</p>
      <ul class="contact__lines">
        <li>4185 Willowbend Rd unit K Coral Point</li>
        <li>FL.32990</li>
        <li>Phone : 321-555-0187</li>
        <li>Fax : 321-555-0162</li>
      </ul>
    </div>
    <div class="license">License : CRC5871642</div>
  </section>
</main>
</body>
</html>
```